Give us a remarkable appearance

We need a unique, remarkable stationery design (Business Cards, Business Letters, Email Signature etc.). The design should use our logo.

Veltro-Consulting is a startup in consulting, management and IT services and individual software development for the financial industry.

Veltro in english is agate stone. We would like to see designs that use colors out of the agate stone color range.

Preferred COLORS: gold, dark red (burgundy), white, dark grey, black ** see attached Logos **

The used font should be available for further usage with texts etc.

The design should express: modernity, precious, high quality, lightness, stability, ecological awareness, speedy, reliability, simplicity, sustainability.

Target Market(s)

C-Level and Business Clients, Professionals

Industry/Entity Type

Business

Logo Text

Logo styles of interest
Pictorial/Combination Logo
Abstract Logo
Wordmark Logo
Requirements
Must have
• Business Cards, Business Papers, Email Signature
Nice to have
• Door plate, Flyersheet (basic structure), Envelop...

```html
<!DOCTYPE html>
<html lang="en">
<head>
<meta charset="utf-8">
<title>Veltro Consulting – Stationery</title>
<link rel="stylesheet" href="https://fonts.googleapis.com/css2?family=Exo+2:wght@400;500;600;700&display=swap">
<style>
  :root {
    --backdrop: #333333;
    --paper: #ffffff;
    --charcoal: #3d3d3d;
    --red: #a31a22;
    --gold: #d39e55;
    --burgundy: #620420;
    --brand-yellow: #f2d21b;
    --ink: #333333;
  }
  * { box-sizing: border-box; margin: 0; padding: 0; }
  html, body { width: 1200px; height: 1200px; overflow: hidden; }
  body {
    background: var(--backdrop);
    font-family: "Exo 2", sans-serif;
    color: var(--ink);
    position: relative;
  }
  .sheet, .card { position: absolute; background: var(--paper); box-shadow: 0 6px 18px rgba(0,0,0,.45); }
  .block { position: absolute; }
  .charcoal { background: var(--charcoal); }
  .red { background: var(--red); }
  .gold { background: var(--gold); }
  .burgundy { background: var(--burgundy); }

  /* Letterhead */
  .letterhead { left: 138px; top: 54px; width: 574px; height: 744px; }
  .letterhead .charcoal { left: 459px; top: 27px; width: 96px; height: 22px; }
  .letterhead .red { left: 459px; top: 49px; width: 96px; height: 46px; }
  .letterhead .gold { left: 459px; top: 102px; width: 94px; height: 24px; }
  .letterhead .burgundy { left: 459px; top: 126px; width: 94px; height: 603px; }
  .side-brand {
    position: absolute; left: 506px; top: 640px;
    transform: rotate(-90deg); transform-origin: left top;
    display: flex; align-items: center; gap: 10px;
    color: var(--brand-yellow); white-space: nowrap;
  }
  .brand-mark { width: 14px; height: 14px; background: var(--brand-yellow); }
  .brand-name { font-weight: 700; font-size: 26px; letter-spacing: 7px; line-height: 1; }
  .brand-sub { font-weight: 500; font-size: 12px; letter-spacing: 4px; }
  .letterhead-footer {
    position: absolute; left: 33px; top: 717px;
    font-size: 7.5px; font-weight: 600; color: var(--ink); white-space: nowrap;
  }
  .letterhead-footer .web { color: var(--burgundy); margin-left: 10px; font-weight: 700; }

  /* Business card front */
  .card-front { left: 91px; top: 868px; width: 471px; height: 273px; }
  .card-front .charcoal { left: 24px; top: 29px; width: 30px; height: 126px; }
  .card-front .red { left: 54px; top: 29px; width: 62px; height: 126px; }
  .card-front .gold { left: 123px; top: 29px; width: 35px; height: 126px; }
  .card-front .burgundy { left: 158px; top: 29px; width: 283px; height: 126px; }
  .card-brand {
    position: absolute; left: 175px; top: 29px; width: 266px; height: 126px;
    display: flex; align-items: center; justify-content: center; gap: 12px;
    color: var(--brand-yellow);
  }
  .card-brand .stack { display: flex; flex-direction: column; align-items: center; }
  .card-brand .brand-name { font-size: 30px; letter-spacing: 8px; }
  .card-brand .brand-sub { font-size: 15px; letter-spacing: 5px; }
  .person { position: absolute; left: 0; width: 100%; text-align: center; }
  .person-name { top: 176px; font-size: 20px; font-weight: 700; color: var(--burgundy); }
  .person-role { top: 197px; font-size: 16px; font-weight: 500; }
  .person-email { top: 236px; font-size: 13px; letter-spacing: .5px; }

  /* Business card back */
  .card-back { left: 614px; top: 861px; width: 472px; height: 284px; }
  .contact { position: absolute; left: 0; width: 100%; text-align: center; font-size: 13px; font-weight: 500; line-height: 17px; }
  .contact-web { top: 100px; color: var(--burgundy); font-weight: 700; letter-spacing: 1.5px; }
  .contact-address { top: 127px; }
  .contact-phone { top: 192px; font-size: 12.5px; }
  .contact-phone b { font-weight: 700; }
  .card-back .red { left: 48px; top: 247px; width: 65px; height: 16px; }
  .card-back .gold { left: 120px; top: 247px; width: 37px; height: 16px; }
  .card-back .burgundy { left: 157px; top: 247px; width: 294px; height: 16px; }
</style>
</head>
<body>
  <section class="sheet letterhead" aria-label="Letterhead">
    <div class="block charcoal"></div>
    <div class="block red"></div>
    <div class="block gold"></div>
    <div class="block burgundy"></div>
    <div class="side-brand">
      <span class="brand-mark"></span>
      <span class="brand-name">VELTRO</span>
      <span class="brand-sub">consulting</span>
    </div>
    <p class="letterhead-footer">1800 Stone Plaza &nbsp;22 North Mill Street Columbus, Ohio 43215 <span class="web">www.veltroconsulting.com</span></p>
  </section>

  <section class="card card-front" aria-label="Business card front">
    <div class="block charcoal"></div>
    <div class="block red"></div>
    <div class="block gold"></div>
    <div class="block burgundy"></div>
    <div class="card-brand">
      <span class="brand-mark"></span>
      <div class="stack">
        <span class="brand-name">VELTRO</span>
        <span class="brand-sub">consulting</span>
      </div>
    </div>
    <p class="person person-name">Daniel Hart</p>
    <p class="person person-role">Director</p>
    <p class="person person-email">hart@veltroconsulting.com</p>
  </section>

  <section class="card card-back" aria-label="Business card back">
    <p class="contact contact-web">www.veltroconsulting.com</p>
    <p class="contact contact-address">1800 Stone Plaza<br>22 North Mill Street<br>Columbus, Ohio 43215</p>
    <p class="contact contact-phone">614 555 0140 <b>Cell</b> &nbsp;.&nbsp; 614 555 0141 <b>Fax</b></p>
    <div class="block red"></div>
    <div class="block gold"></div>
    <div class="block burgundy"></div>
  </section>
</body>
</html>
```